Legal Service Estimated Retainer and Average Case Value

We need an 11x14 flyer that contains the standard retainers and average cost be case, both provided in documents, for each case type we handle. We need the information displayed, preferably in a way that makes the information readable but less troubling to a client shocked at price of litigation. We need one sheet with the retainers and average case value merged into one table.

Target Market(s)

Potential Clients

Font styles to use
Serif
Sans Serif

```html
<!DOCTYPE html>
<html lang="en">
<head>
<meta charset="utf-8">
<title>Legal Service Estimated Retainer and Average Case Value – Flyer Options</title>
<link rel="stylesheet" href="https://fonts.googleapis.com/css2?family=Fira+Sans:wght@400;500;600&family=Open+Sans:wght@400&family=Source+Sans+3:wght@400&family=Tinos:wght@700&display=swap">
<style>
  :root {
    --navy: #1a2350;
    --stripe: #dcdee8;
    --ink: #15182b;
    --rule: #2a2a2a;
    --paper: #ffffff;
    --label: #ffffff;
  }
  * { box-sizing: border-box; margin: 0; padding: 0; }
  html, body { width: 1200px; height: 766px; overflow: hidden; }
  body {
    position: relative;
    background: linear-gradient(180deg, #8e8e8e 0%, #7b7b7b 22%, #3a3a3a 45%, #141414 60%, #5a5a5a 78%, #8a8a8a 92%, #909090 100%);
    font-family: "Source Sans 3", sans-serif;
  }
  .option-label {
    position: absolute; top: 10px; width: 472px;
    text-align: center; color: var(--label);
    font-family: "Open Sans", sans-serif; font-size: 50px; line-height: 62px;
  }
  .option-label--one { left: 91px; }
  .option-label--two { left: 640px; }

  .flyer {
    position: absolute; top: 81px; width: 472px; height: 601px;
    background: var(--paper); color: var(--navy);
  }
  .flyer--striped { left: 91px; }
  .flyer--ruled { left: 640px; }

  .firm-mark {
    position: absolute; top: 24px; left: 0; width: 100%;
    display: flex; justify-content: center; align-items: center; gap: 10px;
  }
  .firm-mark__square { width: 40px; height: 40px; background: var(--navy); }
  .firm-mark__name {
    font-family: "Tinos", serif; font-weight: 700; font-size: 17px;
    line-height: 19px; color: var(--navy); letter-spacing: 0.3px;
  }

  .flyer__title {
    position: absolute; top: 87px; left: 0; width: 100%;
    text-align: center; font-family: "Tinos", serif; font-weight: 700;
    font-size: 21px; line-height: 22.5px; letter-spacing: -0.2px; color: var(--navy);
  }
  .flyer__intro {
    position: absolute; top: 138px; left: 30px; width: 412px;
    text-align: center; font-size: 11px; line-height: 13.6px; color: var(--ink);
  }

  .fee-table {
    position: absolute; border-collapse: collapse; table-layout: fixed;
    font-family: "Fira Sans", sans-serif; font-size: 12px; color: var(--ink);
  }
  .flyer--striped .fee-table { top: 208px; left: 26px; width: 427px; }
  .flyer--ruled .fee-table { top: 205px; left: 23px; width: 433px; }
  .fee-table col.col-case { width: 220px; }
  .fee-table col.col-retainer { width: 94px; }
  .fee-table th {
    text-align: left; vertical-align: top; font-weight: 500;
    font-size: 12px; line-height: 15px; padding: 3px 0 0 11px;
  }
  .fee-table th.case-head { padding-left: 18px; }
  .flyer--striped .fee-table thead tr { background: var(--navy); height: 35px; }
  .flyer--striped .fee-table th { color: #fff; }
  .flyer--striped .fee-table thead + tbody tr:first-child td { border-top: 6px solid #fff; }
  .flyer--ruled .fee-table thead tr { height: 40px; }
  .flyer--ruled .fee-table th { color: var(--ink); padding-top: 6px; font-weight: 600; }

  .fee-table td {
    vertical-align: top; line-height: 15px; padding: 2.5px 0 2px 11px;
  }
  .fee-table tr.single { height: 19.4px; }
  .fee-table tr.double { height: 34.6px; }
  .fee-table td.case {
    position: relative; font-weight: 600; padding-left: 18px;
  }
  .fee-table td.case::before {
    content: ""; position: absolute; left: 6px; top: 7px;
    width: 4px; height: 4px; background: var(--navy);
  }
  .flyer--striped .fee-table tbody tr:nth-child(odd) { background: var(--stripe); }
  .flyer--ruled .fee-table th,
  .flyer--ruled .fee-table td { border: 1px solid var(--rule); }
  .fee-note { font-size: 6.5px; letter-spacing: 0.1px; }

  .contact-bar {
    position: absolute; left: 0; bottom: 0; width: 100%; height: 27px;
    background: var(--navy); color: #fff;
    display: flex; align-items: center; justify-content: center; gap: 10px;
    font-family: "Fira Sans", sans-serif; font-weight: 600; font-size: 13px;
  }
  .contact-bar__item { display: flex; align-items: center; gap: 4px; }
  .contact-bar svg { width: 13px; height: 13px; }
</style>
</head>
<body>

<div class="option-label option-label--one">Design 1</div>
<div class="option-label option-label--two">Design 2</div>

<!-- Option one: striped rows -->
<section class="flyer flyer--striped">
  <div class="firm-mark">
    <span class="firm-mark__square"></span>
    <span class="firm-mark__name">THE LAW OFFICE OF<br>DANIEL M WHITFORD</span>
  </div>
  <h1 class="flyer__title">LEGAL SERVICE ESTIMATED RETAINER<br>AND AVERAGE CASE VALUE</h1>
  <p class="flyer__intro">In order for our clients to set expectations for legal fees, we provide the national average range of fees per case type. These are only to provide you with an understanding of what other cases have cost clients in similar cases. Please note these are not estimates nor guarantees of your own legal costs.</p>
  <table class="fee-table">
    <colgroup><col class="col-case"><col class="col-retainer"><col class="col-fee"></colgroup>
    <thead>
      <tr><th class="case-head">Case Type</th><th>Retainers<br>Total Cost</th><th>Average Fee<br>Per Case Type</th></tr>
    </thead>
    <tbody>
      <tr class="single"><td class="case">Divorce (3301 C)</td><td>$2,000</td><td>$1,500 - $3,000</td></tr>
      <tr class="single"><td class="case">Divorce (3301 D)</td><td>$2,500</td><td>$2,000 - $3,000</td></tr>
      <tr class="single"><td class="case">Divorce and Custody</td><td>$3,500</td><td>$5,000 - $8,000</td></tr>
      <tr class="double"><td class="case">Divorce and Equitable<br>Distribution</td><td>$3,500</td><td>$6,000 - $10,000</td></tr>
      <tr class="single"><td class="case">Divorce and Support</td><td>$3,000</td><td>$2,000 - $4,000</td></tr>
      <tr class="single"><td class="case">Divorce, Custody and Support</td><td>$3,500</td><td>$8,000 - $12,000</td></tr>
      <tr class="double"><td class="case">Divorce, Equitable<br>Distribution and Support</td><td>$3,500</td><td>$8,000 - $12,000</td></tr>
      <tr class="double"><td class="case">Divorce, Equitable<br>Distribution and Custody</td><td>$5,000</td><td>$10,000 - $15,000</td></tr>
      <tr class="double"><td class="case">Divorce, Equitable Distribution,<br>Custody and Support</td><td>$3,500</td><td>$12,000 - $15,000</td></tr>
      <tr class="single"><td class="case">Custody Initial Order</td><td>$3,000</td><td>$4,000 - $7,000</td></tr>
      <tr class="single"><td class="case">Custody Modification</td><td>$3,500</td><td>$5,000 - $8,000</td></tr>
      <tr class="single"><td class="case">Custody and Support</td><td>$3,000</td><td>$5,000 - $8,000</td></tr>
      <tr class="single"><td class="case">(PFA) Protection From Abuse</td><td>$2,000 <span class="fee-note">Paid In Full</span></td><td>$1,500 - $3,000</td></tr>
    </tbody>
  </table>
  <footer class="contact-bar">
    <span class="contact-bar__item">
      <svg viewBox="0 0 16 16" fill="none" stroke="#fff" stroke-width="1.4"><circle cx="8" cy="8" r="6.5"/><ellipse cx="8" cy="8" rx="3" ry="6.5"/><line x1="1.5" y1="8" x2="14.5" y2="8"/></svg>
      www.whitfordfamilylaw.com
    </span>
    <span class="contact-bar__item">
      <svg viewBox="0 0 16 16" fill="#fff"><path d="M4.2 1.5l2 2.6-1.2 1.6c.8 1.8 2.2 3.3 4.1 4.2l1.6-1.2 2.6 2-1.3 2.3C7.5 13 3 8.5 2 3.2z"/></svg>
      (555) 014-2736
    </span>
  </footer>
</section>

<!-- Option two: ruled grid -->
<section class="flyer flyer--ruled">
  <div class="firm-mark">
    <span class="firm-mark__square"></span>
    <span class="firm-mark__name">THE LAW OFFICE OF<br>DANIEL M WHITFORD</span>
  </div>
  <h1 class="flyer__title">LEGAL SERVICE ESTIMATED RETAINER<br>AND AVERAGE CASE VALUE</h1>
  <p class="flyer__intro">In order for our clients to set expectations for legal fees, we provide the national average range of fees per case type. These are only to provide you with an understanding of what other cases have cost clients in similar cases. Please note these are not estimates nor guarantees of your own legal costs.</p>
  <table class="fee-table">
    <colgroup><col class="col-case"><col class="col-retainer"><col class="col-fee"></colgroup>
    <thead>
      <tr><th class="case-head">Case Type</th><th>Retainers<br>Total Cost</th><th>Average Fee<br>Per Case Type</th></tr>
    </thead>
    <tbody>
      <tr class="single"><td class="case">Divorce (3301 C)</td><td>$2,000</td><td>$1,500 - $3,000</td></tr>
      <tr class="single"><td class="case">Divorce (3301 D)</td><td>$2,500</td><td>$2,000 - $3,000</td></tr>
      <tr class="single"><td class="case">Divorce and Custody</td><td>$3,500</td><td>$5,000 - $8,000</td></tr>
      <tr class="double"><td class="case">Divorce and Equitable<br>Distribution</td><td>$3,500</td><td>$6,000 - $10,000</td></tr>
      <tr class="single"><td class="case">Divorce and Support</td><td>$3,000</td><td>$2,000 - $4,000</td></tr>
      <tr class="single"><td class="case">Divorce, Custody and Support</td><td>$3,500</td><td>$8,000 - $12,000</td></tr>
      <tr class="double"><td class="case">Divorce, Equitable<br>Distribution and Support</td><td>$3,500</td><td>$8,000 - $12,000</td></tr>
      <tr class="double"><td class="case">Divorce, Equitable<br>Distribution and Custody</td><td>$5,000</td><td>$10,000 - $15,000</td></tr>
      <tr class="double"><td class="case">Divorce, Equitable Distribution,<br>Custody and Support</td><td>$3,500</td><td>$12,000 - $15,000</td></tr>
      <tr class="single"><td class="case">Custody Initial Order</td><td>$3,000</td><td>$4,000 - $7,000</td></tr>
      <tr class="single"><td class="case">Custody Modification</td><td>$3,500</td><td>$5,000 - $8,000</td></tr>
      <tr class="single"><td class="case">Custody and Support</td><td>$3,000</td><td>$5,000 - $8,000</td></tr>
      <tr class="single"><td class="case">(PFA) Protection From Abuse</td><td>$2,000 <span class="fee-note">Paid In Full</span></td><td>$1,500 - $3,000</td></tr>
    </tbody>
  </table>
  <footer class="contact-bar">
    <span class="contact-bar__item">
      <svg viewBox="0 0 16 16" fill="none" stroke="#fff" stroke-width="1.4"><circle cx="8" cy="8" r="6.5"/><ellipse cx="8" cy="8" rx="3" ry="6.5"/><line x1="1.5" y1="8" x2="14.5" y2="8"/></svg>
      www.whitfordfamilylaw.com
    </span>
    <span class="contact-bar__item">
      <svg viewBox="0 0 16 16" fill="#fff"><path d="M4.2 1.5l2 2.6-1.2 1.6c.8 1.8 2.2 3.3 4.1 4.2l1.6-1.2 2.6 2-1.3 2.3C7.5 13 3 8.5 2 3.2z"/></svg>
      (555) 014-2736
    </span>
  </footer>
</section>

</body>
</html>
```